PLUMBING POSTCARD DESIGN (MARKETING)

We are a local Plumbing business , Needing a post card to market domestic plumbing maintenance in my local area. The post card will have a magnet business card attached so allowance in design will need to be made. I have a slogan i want Incorporated into the design and is "TRY THE BEST, FLUSH THE REST"
I have attached my company name and logo to also incorporate into the design.
post card size 21cm L x 10cm H
business magnet card that will be attached to post card is 9cm L X 5.5cm H.
Post card will be one sided and will need following text inserted into design:
Pipevale would like to offer its fellow locals $40 off their next plumbing job. We pride ourselves in supplying the highest level of workmanship at the most competitive prices. CALL US TODAY
0431 582 907
Target Market(s)
Property owners (domestic market0
Industry/Entity Type
Plumbing
Requirements
Must have
- Eye catching, Slogan, company name and logo

```html
<!DOCTYPE html>
<html lang="en">
<head>
<meta charset="utf-8">
<title>Pipevale Postcard</title>
<link rel="stylesheet" href="https://fonts.googleapis.com/css2?family=Raleway:wght@400;600;700&family=Arimo:wght@400;700&display=swap">
<style>
  :root {
    --page-bg: #5d5d5d;
    --card-bg: #d9d7d8;
    --brand-blue: #2a8bbd;
    --brand-blue-light: #27aedc;
    --brand-orange: #f2873a;
    --brand-orange-light: #f7a93f;
    --ink-grey: #5a5a5a;
    --frame-grey: #4a4a4a;
    --placeholder-grey: #a8a8a8;
  }
  * { box-sizing: border-box; margin: 0; padding: 0; }
  html, body {
    width: 1200px;
    height: 673px;
    overflow: hidden;
    background: var(--page-bg);
  }
  .postcard {
    position: absolute;
    left: 50px;
    top: 77px;
    width: 1100px;
    height: 518px;
    background: var(--card-bg);
    overflow: hidden;
  }
  .brand-band {
    position: absolute;
    left: 505px;
    top: 0;
    width: 380px;
    height: 518px;
    background: linear-gradient(180deg, var(--brand-blue) 0%, var(--brand-blue-light) 45%, var(--brand-orange) 75%, var(--brand-orange-light) 100%);
    opacity: 0.85;
  }
  .brand-lockup {
    position: absolute;
    left: 44px;
    top: 48px;
    display: flex;
    align-items: center;
    gap: 14px;
  }
  .brand-dot {
    width: 34px;
    height: 34px;
    border-radius: 50%;
    background: var(--brand-blue);
  }
  .brand-name {
    font-family: "Raleway", sans-serif;
    font-weight: 700;
    font-size: 54px;
    letter-spacing: 1px;
    color: var(--ink-grey);
    text-transform: uppercase;
    line-height: 1;
  }
  .offer-copy {
    position: absolute;
    left: 43px;
    top: 178px;
    width: 418px;
    font-family: "Raleway", sans-serif;
    font-weight: 400;
    font-size: 20.5px;
    line-height: 27px;
    color: var(--ink-grey);
    text-align: justify;
  }
  .call-heading {
    position: absolute;
    left: 43px;
    top: 330px;
    font-family: "Arimo", sans-serif;
    font-weight: 700;
    font-size: 41px;
    color: var(--brand-blue);
    line-height: 1;
  }
  .phone-number {
    position: absolute;
    left: 43px;
    top: 384px;
    font-family: "Arimo", sans-serif;
    font-weight: 400;
    font-size: 40px;
    color: var(--brand-blue);
    line-height: 1;
  }
  .slogan {
    position: absolute;
    left: 40px;
    top: 437px;
    font-family: "Raleway", sans-serif;
    font-weight: 700;
    font-size: 31px;
    color: var(--brand-orange);
    line-height: 1;
  }
  .magnet-area {
    position: absolute;
    left: 532px;
    top: 130px;
    width: 562px;
    height: 297px;
    border: 3px solid var(--frame-grey);
    border-radius: 14px;
    background: var(--card-bg);
    display: flex;
    align-items: center;
    justify-content: center;
    font-family: "Raleway", sans-serif;
    font-size: 20px;
    color: var(--placeholder-grey);
  }
</style>
</head>
<body>
  <main class="postcard">
    <div class="brand-band" role="img" aria-label="Decorative brand colour sweep in blue and orange"></div>

    <div class="brand-lockup">
      <span class="brand-dot"></span>
      <span class="brand-name">Pipevale</span>
    </div>

    <p class="offer-copy">Pipevale would like to offer its fellow locals $40 off their next plumbing job. We pride ourselves in supplying the highest level of workmanship at the most competitive prices.</p>

    <h2 class="call-heading">CALL US TODAY</h2>
    <p class="phone-number">0431 582 907</p>
    <p class="slogan">TRY THE BEST, FLUSH THE REST</p>

    <div class="magnet-area">Magnet Area</div>
  </main>
</body>
</html>
```